依頼詳細
昨年11月より発売していますが、大変好調に売れています。
この3月より、リボンタイプのポケ&ミントを追加発売するため、より一層拡販したくA3サイズのポスターを作成する運びとなりました。用途としましては、マルセリオン、青峰ツールズ、ハーバーランタンズ、ドラッグストアー、モバイルショップさんなどで販売していただく際に、今回のポスターを見て一般顧客様にこの商品の良さをわかっていただき、購入に至る という宣伝のポスターになります。 一見、ただのスマホポーチに見えてしまうのですが、裏には特殊シートを採用しておりスマホを入れたまま操作ができる というポイントを、しっかりポスターに表現して頂きたいです。
ターゲットは20代~40代の女性ですので宜しくお願いします。
記載項目
下記URLより商品をイメージをしてください。
http://www.kk-hotaru-example.jp/items/pokemint/index.html
http://www.kk-hotaru-example.jp/items/3stylecase_frill/index.html
スマホを入れたまま さわる、話せる をキーワードに。お願いします。
他にキャッチコピーを作っていただいてもいいです。 ある意味自由に表現して頂いて、この新商品を輝かせてください。

サイズ
A3
ページ数
片面
希望イメージ
シンプル 複雑
単色 カラフル
暗い 明るい
日常 高級
遊び心 厳粛
未来的 伝統的
女性的 男性的
希望する色
ピンク、オレンジ
納品ファイル
• 高解像度JPG (.jpg)
• イラストレーター形式 (.ai)
補足説明
弊社ホームページ  http://www.kk-hotaru-example.jp
お世話になります。

別モデルにて撮影致しましたので、添付ファイルを追加させていただき、

締め切り時間を延長させていただきます。

できましたら、新モデル画像の素材をメインで使っていただけると嬉しいです。

宜しくお願い致します。
■ 選んだ理由

商品の魅力にあう写真配列を自然な感じで引き出して頂き、
私もこの商品を持ちたいと感じさせてくれるデザインでしたので、
選ばせて頂きました。

商品のコンセプトイメージ一番合っていると思いました。

■ 提案者全員のお礼・コメント

今回はたくさんのご提案をいただきましてありがとうございました。
初めて依頼させていただきまして、提案が来る度、凄い楽しみに待っていました。
我々が考えていたデザイン以上の提案ばかりでしたので、色々と勉強になりました。

弊社ではいろいろと商品企画を行っていましてまた依頼させていただく事があると思いますので、
今後ともよろしくお願い致します。
この度はありがとうございました。

```html
<!DOCTYPE html>
<html lang="ja">
<head>
<meta charset="utf-8">
<title>ポケ&ミント スマートフォン専用ポーチ</title>
<link rel="stylesheet" href="https://fonts.googleapis.com/css2?family=Great+Vibes&family=Noto+Sans+JP:wght@500;700;900&display=swap">
<style>
:root{
  --pink-deep:#d9417f;
  --pink-mid:#ee8fb5;
  --pink-light:#fbe0ec;
  --pink-glow:#fff3f8;
  --red-badge:#e2262f;
  --ink:#2a1a22;
  --white:#ffffff;
  --photo-warm:#d9b59c;
  --photo-dark:#5a4034;
}
*{margin:0;padding:0;box-sizing:border-box}
html,body{width:846px;height:1200px;overflow:hidden}
body{font-family:"Noto Sans JP",sans-serif;color:var(--ink)}
.poster{
  position:relative;width:846px;height:1200px;overflow:hidden;
  background:radial-gradient(ellipse at 55% 45%,var(--pink-glow) 0%,var(--pink-light) 35%,var(--pink-mid) 75%,var(--pink-deep) 100%);
}
.photo{position:absolute}
.photo-standing{left:330px;top:0;width:320px;height:690px;border-radius:140px 140px 40px 40px;
  background:linear-gradient(180deg,var(--photo-dark) 0%,var(--photo-warm) 30%,var(--white) 55%,var(--photo-warm) 80%,rgba(217,181,156,0) 100%);opacity:.85}
.photo-bag{left:0;top:420px;width:480px;height:480px;border-radius:0 200px 40px 0;
  background:linear-gradient(160deg,var(--photo-dark) 0%,var(--photo-warm) 35%,#9b6a4a 70%,rgba(155,106,74,0) 100%);opacity:.8}
.photo-call{left:495px;top:640px;width:351px;height:280px;border-radius:150px 0 0 40px;
  background:linear-gradient(200deg,var(--photo-dark) 0%,var(--photo-warm) 45%,rgba(217,181,156,0) 100%);opacity:.85}
.category-band{position:absolute;z-index:2;left:85px;top:36px;width:340px;height:30px;background:var(--pink-deep);
  color:var(--white);font-weight:700;font-size:20px;letter-spacing:.12em;text-align:center;line-height:30px}
.brand-title{position:absolute;z-index:1;left:30px;top:100px;font-family:"Great Vibes",cursive;font-weight:400;color:var(--pink-deep);
  line-height:.85;text-shadow:0 0 6px var(--white),0 0 2px var(--white)}
.brand-title .word{display:block;font-size:130px}
.brand-title .amp{display:block;font-size:96px;padding-left:100px}
.brand-title .word.last{padding-left:30px}
.launch-badge{position:absolute;left:668px;top:68px;width:120px;height:120px;border-radius:50%;background:var(--red-badge);
  color:var(--white);font-weight:900;font-size:30px;display:flex;align-items:center;justify-content:center;border:4px solid var(--white)}
.headline{position:absolute;z-index:2;right:24px;top:200px;text-align:right;font-weight:900;font-size:44px;line-height:1.4;color:var(--ink);
  text-shadow:0 0 8px var(--white)}
.feature{position:absolute;width:150px;height:150px;border-radius:50%;background:var(--white);border:5px solid var(--pink-deep);
  display:flex;flex-direction:column;align-items:center;justify-content:center;text-align:center}
.feature .label{font-weight:900;font-size:32px;color:var(--pink-deep)}
.feature .note{font-size:11px;line-height:1.35;margin-top:4px;color:var(--ink)}
.feature-touch{left:495px;top:900px}
.feature-talk{left:665px;top:870px}
.body-copy{position:absolute;left:40px;top:910px;width:340px;font-weight:700;font-size:18px;line-height:1.6;color:var(--white);
  text-shadow:0 0 3px rgba(120,20,60,.6)}
.colour-range{position:absolute;left:480px;top:1062px;width:350px}
.colour-range .caption{font-weight:700;font-size:16px;color:var(--white);text-shadow:0 0 3px rgba(120,20,60,.6);margin-bottom:6px}
.swatches{display:grid;grid-template-columns:repeat(6,1fr);gap:5px}
.swatch{height:28px;border:2px solid var(--white)}
</style>
</head>
<body>
<main class="poster">
  <div class="photo photo-standing" role="img" aria-label="ピンクのバラ付きポーチを肩から提げた女性モデルの全身写真"></div>
  <div class="photo photo-bag" role="img" aria-label="茶色のバッグにピンクのポーチを付けた女性モデルの写真"></div>
  <div class="photo photo-call" role="img" aria-label="ポーチに入れたままスマホで通話する女性モデルの写真"></div>

  <div class="category-band">スマートフォン専用ポーチ</div>
  <h1 class="brand-title"><span class="word">Poke</span><span class="amp">&amp;</span><span class="word last">Mint</span></h1>

  <div class="launch-badge">新発売</div>

  <p class="headline">ポーチにいれたまま、<br>スマホが使えます。</p>

  <div class="feature feature-touch">
    <span class="label">さわる</span>
    <span class="note">入れたまま<br>操作ができます</span>
  </div>
  <div class="feature feature-talk">
    <span class="label">話せる</span>
    <span class="note">入れたまま<br>通話ができます</span>
  </div>

  <p class="body-copy">ポーチから取り出さず「さわる」「話せる」新設計のスマートフォン専用ポーチ【ポケ&amp;ミント】2種類の専用ストラップが付属しているので、コーデに合わせて4wayで楽しめます。フォンノヴァ5やステラフォンS3等も入ります。</p>

  <section class="colour-range">
    <p class="caption">◆カラーは全12色</p>
    <div class="swatches" role="img" aria-label="全12色のポーチのカラーバリエーション">
      <span class="swatch" style="background:#3a3a3a"></span>
      <span class="swatch" style="background:#7a5a44"></span>
      <span class="swatch" style="background:#c9b8a3"></span>
      <span class="swatch" style="background:#d8d2c8"></span>
      <span class="swatch" style="background:#6b6e78"></span>
      <span class="swatch" style="background:#a78a70"></span>
      <span class="swatch" style="background:#c8d8ee"></span>
      <span class="swatch" style="background:#b9a4d4"></span>
      <span class="swatch" style="background:#e88ab0"></span>
      <span class="swatch" style="background:#d64a86"></span>
      <span class="swatch" style="background:#f0ece4"></span>
      <span class="swatch" style="background:#9a2f4c"></span>
    </div>
  </section>
</main>
</body>
</html>
```